Recruitment Site Design

We need a design for the login page, about page, and inner pages of a recruitment site for an oil and gas company. Design should be modern, sleek, professional and colors can be blue, green, white, orange or any other recommended colors.

Please also take into consideration that once the users login, they will need to access a form to fill in their information.

** UPDATE: Kindly provide a design for the inner information page consistent with the outer design. Attached is a picture of the basic structure. ***
Updates

Please provide a design for inner pages as shown in the design brief consistent with the registration page provided. 

Reason: We're extending it to get more inside pages.

Target Market(s)

Professionals looking for a career in the oil and gas industry in the Middle East.

Industry/Entity Type

Oil And Gas

Requirements
Must have
• Sleek design

```html
<!DOCTYPE html>
<html lang="en">
<head>
<meta charset="utf-8">
<title>Register Here – Recruitment</title>
<link href="https://fonts.googleapis.com/css2?family=Ruda:wght@400;700&display=swap" rel="stylesheet">
<style>
  :root{
    --orange:#c0742c;
    --orange-light:#d98a3c;
    --orange-dark:#a95f1f;
    --linen:#e3e3e1;
    --panel:#efefee;
    --line:#d2d2d0;
    --text:#5a5a5a;
    --nav-text:#4a4a4a;
    --white:#ffffff;
    --sky:#6f8fbf;
  }
  *{box-sizing:border-box;margin:0;padding:0}
  html,body{width:1200px;height:768px;overflow:hidden}
  body{position:relative;font-family:"Ruda",Arial,sans-serif;background:var(--linen);color:var(--text)}
  .abs{position:absolute}

  .hero-photo{left:0;top:0;width:1200px;height:135px;
    background:linear-gradient(180deg,#3e5f98 0%,#7f9fcc 45%,#c9d6e6 100%)}
  .nav-band{left:0;top:37px;width:1200px;height:68px;background:rgba(236,238,240,.93)}
  .logo-box{left:185px;top:20px;width:162px;height:103px;border-radius:8px;background:#ececec;
    border:3px solid #f7f7f7;box-shadow:0 1px 4px rgba(0,0,0,.25);
    display:flex;align-items:center;justify-content:center;color:var(--orange);font-size:56px}
  .main-nav{left:490px;top:37px;height:68px;display:flex;align-items:center}
  .main-nav a{font-size:14px;color:var(--nav-text);text-decoration:none;padding:0 28px;height:28px;line-height:28px;border-left:1px solid #c9c9c9}
  .main-nav a:first-child{border-left:none;padding-left:17px}
  .main-nav a.current{color:var(--orange)}

  .form-panel{left:172px;top:153px;width:858px;height:361px;border-radius:10px;background:#dcdcda;border:1px solid #cfcfcd}
  .form-table{left:183px;top:163px;width:836px;height:340px;background:var(--panel);border:1px solid #d5d5d3}
  .tabs{left:183px;top:163px;width:836px;height:52px;background:linear-gradient(#fafafa,#e9e9e9);border-bottom:1px solid var(--line)}
  .tab{position:absolute;top:0;height:52px;display:flex;align-items:center;font-size:15px;color:#555}
  .tab svg{margin-left:10px}
  .row-line{left:184px;width:834px;height:1px;background:var(--line)}
  .col-line{left:603px;top:215px;width:1px;height:288px;background:var(--line)}
  .field{left:230px;width:330px;height:38px;border-radius:6px;border:1px solid #c4c4c4;background:var(--white);
    box-shadow:inset 0 1px 2px rgba(0,0,0,.08);font-size:12px;color:#666;padding-left:9px;display:flex;align-items:center}
  .label{left:642px;font-size:12px;color:#666}
  .select{left:773px;width:199px;height:38px;border-radius:4px;border:1px solid #c4c4c4;background:var(--white);
    font-size:12px;color:#555;padding-left:8px;display:flex;align-items:center;overflow:hidden}
  .select .arrow{position:absolute;right:0;top:0;width:38px;height:36px;background:linear-gradient(var(--orange-light),var(--orange));display:flex;align-items:center;justify-content:center}
  .radio{display:flex;align-items:center;font-size:12px;color:#666;top:295px}
  .radio i{width:15px;height:15px;border-radius:50%;background:radial-gradient(#b5b5b5,#8e8e8e);border:1px solid #8a8a8a;margin-right:7px;display:inline-block}
  .radio i.on{background:radial-gradient(#fff 0 3px,#999 4px)}
  .next-btn{left:868px;top:453px;width:104px;height:40px;border-radius:6px;background:linear-gradient(var(--orange-light),var(--orange-dark));
    color:var(--white);font-size:15px;font-weight:700;display:flex;align-items:center;justify-content:center;box-shadow:0 1px 2px rgba(0,0,0,.3)}

  .site-photo{left:0;top:532px;width:1200px;height:45px;background:linear-gradient(90deg,#6f6e6a,#9a9893 40%,#b7b3a6 70%,#7c8a55)}
  .footer{left:0;top:576px;width:1200px;height:192px;background:var(--orange);border-top:3px solid var(--orange-dark);color:var(--white)}
  .footer-tab{left:543px;top:540px}
  .footer h2{position:absolute;left:174px;top:14px;font-size:19px;font-weight:400}
  .footer hr{position:absolute;left:174px;top:46px;width:842px;border:none;border-top:1px solid rgba(255,255,255,.45)}
  .footer p{position:absolute;left:174px;top:54px;width:848px;font-size:12.3px;line-height:20px;text-shadow:0 1px 1px rgba(0,0,0,.2)}
  .copyright{position:absolute;left:500px;top:150px;width:238px;text-align:center;font-size:11.5px;line-height:15px}
  .social{position:absolute;top:159px;display:flex;gap:5px;left:863px}
  .social span{width:16px;height:16px;border-radius:2px;background:#e9d2b8}
</style>
</head>
<body>
  <div class="abs hero-photo" role="img" aria-label="Photo of an oil field worker in a hard hat under a blue sky"></div>
  <div class="abs nav-band"></div>
  <div class="abs logo-box">Logo</div>
  <nav class="abs main-nav">
    <a href="#">Home</a><a href="#">About Us</a><a href="#">Find Job</a><a href="#" class="current">Register Here</a><a href="#">Contact Us</a>
  </nav>

  <div class="abs form-panel"></div>
  <div class="abs form-table"></div>
  <div class="abs tabs">
    <svg class="abs" style="left:0;top:0" width="225" height="52"><polygon points="0,0 210,0 224,26 210,52 0,52" fill="#c0742c"/></svg>
    <svg class="abs" style="left:210px;top:0" width="255" height="52"><polyline points="0,0 14,26 0,52" fill="none" stroke="#d6d6d6" stroke-width="2"/><polyline points="240,0 254,26 240,52" fill="none" stroke="#d6d6d6" stroke-width="2"/></svg>
    <div class="tab" style="left:47px;color:#fff">Basic Information
      <svg width="20" height="16"><rect x="1" y="2" width="18" height="13" rx="2" fill="none" stroke="#fff" stroke-width="1.5"/><rect x="4" y="6" width="4" height="5" fill="#fff"/><rect x="10" y="6" width="6" height="1.5" fill="#fff"/><rect x="10" y="9" width="6" height="1.5" fill="#fff"/></svg></div>
    <div class="tab" style="left:248px">Academic Information
      <svg width="20" height="16"><rect x="1" y="4" width="18" height="12" rx="1" fill="#c8c8c8"/><rect x="7" y="1" width="6" height="4" fill="none" stroke="#c8c8c8" stroke-width="1.5"/></svg></div>
    <div class="tab" style="left:486px">Proffesional Information
      <svg width="20" height="18"><circle cx="10" cy="5" r="4" fill="#c8c8c8"/><path d="M2 18 Q2 10 10 10 Q18 10 18 18Z" fill="#c8c8c8"/></svg></div>
  </div>

  <div class="abs row-line" style="top:272px"></div>
  <div class="abs row-line" style="top:330px"></div>
  <div class="abs row-line" style="top:388px"></div>
  <div class="abs row-line" style="top:445px"></div>
  <div class="abs col-line"></div>

  <div class="abs field" style="top:225px">First Name</div>
  <div class="abs field" style="top:282px">Last Name</div>
  <div class="abs field" style="top:341px">Date of Birth</div>
  <div class="abs field" style="top:398px">Place of Birth</div>
  <div class="abs field" style="top:455px">Nationality</div>

  <div class="abs label" style="top:237px">Additional Nationality:</div>
  <div class="abs select" style="top:225px">Select Country<span class="arrow"><svg width="14" height="9"><polygon points="0,0 14,0 7,9" fill="#fff"/></svg></span></div>
  <div class="abs label" style="top:295px">Sex:</div>
  <div class="abs radio" style="left:775px"><i></i>Male</div>
  <div class="abs radio" style="left:849px"><i class="on"></i>Female</div>
  <div class="abs label" style="top:353px">Status:</div>
  <div class="abs select" style="top:341px">Single<span class="arrow"><svg width="14" height="9"><polygon points="0,0 14,0 7,9" fill="#fff"/></svg></span></div>
  <div class="abs label" style="top:411px">Language Known:</div>
  <div class="abs select" style="top:399px">Choose One or Multiple<span class="arrow"><svg width="14" height="9"><polygon points="0,0 14,0 7,9" fill="#fff"/></svg></span></div>
  <div class="abs next-btn">Next &gt;&gt;</div>

  <div class="abs site-photo" role="img" aria-label="Photo of an oil and gas site with pipe racks and a worker in orange overalls"></div>
  <footer class="abs footer">
    <h2>Welcome to our site</h2>
    <hr>
    <p>We need a design for the login page, about page, and inner pages of a recruitment site for an oil and gas company. Design should be modern, sleek, professional and colors can be blue, green, white, orange or any other recommended colors. We need a design for the login page, about page, and inner pages of a recruitment site for an oil and gas company. Design should be modern, sleek, professional and colors can be blue, green, white, orange or any other recommended colors. We need a design for the login page, about page, and inner pages of a recruitment site for us.</p>
    <div class="copyright">Copyright @ 2012, Company Name<br>Terms &amp; Privacy Policy</div>
    <div class="social"><span></span><span></span></div>
  </footer>
  <svg class="abs footer-tab" width="112" height="38"><path d="M0 38 L14 6 Q16 1 22 1 L90 1 Q96 1 98 6 L112 38Z" fill="#c0742c"/><path d="M10 30 L16 10 Q18 5 24 5 L88 5 Q94 5 96 10 L102 30Z" fill="#d98a3c"/><circle cx="36" cy="18" r="5" fill="#a95f1f"/><circle cx="56" cy="18" r="5" fill="#f3e2cf"/><circle cx="76" cy="18" r="5" fill="#f3e2cf"/></svg>
</body>
</html>
```